Looking for potential sellers

We help people buy and sell homes and are currently looking for potential home sellers. We offer low commissions, are the Local Colorado Springs and Falcon Experts, homes selling fast and at top dollar, Free expert pricing opinions and Consultations, over 9 years of experience, top rated Realtors creative and aggressive marketing strategies. Never merely own a house, THRIVE at Harborview. phone number 482-630-9157 web thriveatharborview.com

```html
<!DOCTYPE html>
<html lang="en">
<head>
<meta charset="utf-8">
<title>Meridian Real Estate – Seller Postcard</title>
<link href="https://fonts.googleapis.com/css2?family=Poppins:wght@400;500;600;700;800&family=Montserrat:wght@400;500&family=Roboto:wght@400;700&display=swap" rel="stylesheet">
<style>
  :root {
    --olive: #a8a56a;
    --slate: #2c323b;
    --white: #ffffff;
    --taupe-light: #b9a696;
    --taupe-dark: #8d7867;
    --ink: #222222;
    --page: #ececea;
  }
  * { box-sizing: border-box; margin: 0; padding: 0; }
  html, body { width: 894px; height: 1200px; overflow: hidden; background: var(--page); }
  body { position: relative; font-family: "Poppins", sans-serif; }

  .card { position: absolute; left: 57px; width: 780px; height: 519px; overflow: hidden; box-shadow: 0 4px 14px rgba(0,0,0,.22); }
  .card--front { top: 50px; background: var(--olive); }
  .card--back { top: 631px; background: var(--white); }

  /* Front */
  .front-photo { position: absolute; inset: 0 0 auto 0; height: 336px; }
  .site-url { position: absolute; top: 12px; right: 20px; color: var(--white); font-weight: 600; font-size: 15px; }
  .brand { position: absolute; display: flex; align-items: center; gap: 8px; color: var(--white); font-weight: 500; white-space: nowrap; }
  .brand__mark { width: 12px; height: 12px; background: var(--white); }
  .front-brand { left: 32px; top: 60px; font-size: 30px; }
  .headline { position: absolute; left: 28px; top: 140px; color: var(--white); font-weight: 800; font-size: 36px; line-height: 1.12; }
  .rule { position: absolute; left: 32px; top: 234px; width: 292px; height: 2px; background: var(--white); }
  .intro { position: absolute; left: 32px; top: 246px; width: 300px; color: var(--white); font-family: "Montserrat", sans-serif; font-size: 10.6px; line-height: 1.4; }

  .benefits { position: absolute; left: 0; top: 336px; width: 780px; height: 163px; background: var(--slate); }
  .benefit { position: absolute; top: 26px; display: flex; align-items: center; gap: 20px; }
  .benefit__icon { width: 54px; height: 54px; background: var(--olive); display: flex; align-items: center; justify-content: center; }
  .benefit__label { font-weight: 700; font-size: 14.5px; line-height: 1.3; color: var(--white); text-transform: uppercase; }
  .benefit__label span { color: var(--olive); display: block; }
  .benefit--1 { left: 38px; } .benefit--2 { left: 267px; } .benefit--3 { left: 511px; }
  .pitch { position: absolute; top: 106px; color: var(--white); font-weight: 400; font-size: 14px; line-height: 1.5; }
  .pitch strong { font-weight: 700; }
  .pitch--1 { left: 33px; } .pitch--2 { left: 276px; } .pitch--3 { left: 600px; }
  .divider { position: absolute; top: 110px; width: 2px; height: 36px; background: var(--white); }
  .divider--1 { left: 254px; } .divider--2 { left: 577px; }
  .footer-strip { position: absolute; left: 0; bottom: 0; width: 780px; height: 20px; background: var(--olive); }

  /* Back */
  .back-panel { position: absolute; left: 0; top: 0; width: 390px; height: 519px; background: linear-gradient(180deg, var(--taupe-dark) 0%, var(--taupe-light) 45%, var(--taupe-dark) 100%); }
  .portrait { position: absolute; left: 0; top: 226px; width: 222px; height: 293px; background: linear-gradient(160deg, #c49a80 0%, #5a5552 70%, #3a3a3e 100%); }
  .back-title { position: absolute; left: 28px; top: 20px; color: var(--white); font-weight: 700; font-size: 36px; }
  .tagline { position: absolute; left: 28px; top: 68px; width: 336px; color: var(--white); font-family: "Montserrat", sans-serif; font-size: 13.4px; font-weight: 500; white-space: nowrap; }
  .story { position: absolute; left: 28px; top: 94px; width: 327px; color: var(--white); font-family: "Montserrat", sans-serif; font-size: 10.4px; line-height: 1.39; text-align: justify; }
  .back-brand { right: 418px; top: 318px; font-size: 26px; }
  .back-contact { position: absolute; right: 418px; top: 364px; text-align: right; color: var(--white); font-weight: 700; white-space: nowrap; }
  .agent { font-size: 16px; }
  .reach { margin-top: 26px; font-size: 14.5px; }
  .phone { font-size: 20px; letter-spacing: 1px; line-height: 1.25; }
  .web { font-size: 15px; }

  .indicia { position: absolute; left: 662px; top: 38px; width: 80px; height: 80px; border: 1px solid var(--ink); font-family: "Roboto", sans-serif; font-size: 10.5px; line-height: 1.3; text-align: center; color: var(--ink); padding-top: 7px; }
  .indicia b { font-weight: 700; }
  .address { position: absolute; left: 477px; top: 186px; width: 264px; height: 82px; border: 1px solid var(--ink); font-family: "Roboto", sans-serif; font-size: 15.5px; line-height: 1.25; color: var(--ink); padding: 27px 0 0 20px; }
</style>
</head>
<body>

<section class="card card--front">
  <svg class="front-photo" width="780" height="336" viewBox="0 0 780 336" role="img" aria-label="Aerial landscape of snowy mountains under a pink sunset sky above a forested lake">
    <defs>
      <linearGradient id="scene" x1="0" y1="0" x2="0" y2="1">
        <stop offset="0" stop-color="#4c4866"/>
        <stop offset="0.3" stop-color="#a4727a"/>
        <stop offset="0.5" stop-color="#7d7280"/>
        <stop offset="0.65" stop-color="#3a4438"/>
        <stop offset="1" stop-color="#26301f"/>
      </linearGradient>
    </defs>
    <polygon points="318,0 780,0 780,336 427,336" fill="url(#scene)"/>
    <polygon points="319,0 324,0 433,336 428,336" fill="#ffffff"/>
  </svg>
  <div class="site-url">thriveatharborview.com</div>

  <div class="brand front-brand"><span class="brand__mark"></span>Meridian</div>
  <h1 class="headline">Looking to Sell<br>Your Home?</h1>
  <div class="rule"></div>
  <p class="intro">There's never been a better time to sell your home in Colorado Springs! With home values rising almost 10% in the last year alone, and predicted to jump another 3.7% within the year, it truly is a seller's market!</p>

  <div class="benefits">
    <div class="benefit benefit--1">
      <div class="benefit__icon">
        <svg width="34" height="30" viewBox="0 0 34 30" fill="none" stroke="#fff" stroke-width="2"><polyline points="3,8 17,26 31,8"/><text x="11" y="17" font-size="11" fill="#fff" stroke="none" font-family="Poppins">%</text></svg>
      </div>
      <div class="benefit__label">Low<span>Commissions</span></div>
    </div>
    <div class="benefit benefit--2">
      <div class="benefit__icon">
        <svg width="38" height="30" viewBox="0 0 38 30" fill="none" stroke="#fff" stroke-width="2"><text x="2" y="21" font-size="16" fill="#fff" stroke="none" font-family="Poppins">$</text><polyline points="14,5 22,15 14,25"/><polyline points="24,5 32,15 24,25"/></svg>
      </div>
      <div class="benefit__label">Fast selling and<span>at top dollar</span></div>
    </div>
    <div class="benefit benefit--3">
      <div class="benefit__icon">
        <svg width="36" height="32" viewBox="0 0 36 32" fill="#fff"><circle cx="12" cy="14" r="5"/><path d="M3 30c0-6 4-9 9-9s9 3 9 9z"/><circle cx="25" cy="7" r="4"/><path d="M18 19c1-5 4-6 7-6s7 2 7 7z"/></svg>
      </div>
      <div class="benefit__label">Free expert pricing<span>consultations</span></div>
    </div>
    <p class="pitch pitch--1">Over 9 years of experience,<br>top rated REALTOR®</p>
    <div class="divider divider--1"></div>
    <p class="pitch pitch--2">Ready to make a change?<br>Contact us to sell your property today!</p>
    <div class="divider divider--2"></div>
    <p class="pitch pitch--3">Get in touch with us<br><strong>482-630-9157</strong></p>
  </div>
  <div class="footer-strip"></div>
</section>

<section class="card card--back">
  <div class="back-panel"></div>
  <div class="portrait" role="img" aria-label="Portrait photo of the lead broker in a dark blazer"></div>
  <h2 class="back-title">It's Time...</h2>
  <p class="tagline">Never merely own a house, THRIVE at Harborview.</p>
  <p class="story">Meridian Real Estate, and our lead broker Dale Carver, have been helping clients find their dream home in beautiful Colorado Springs and its surrounding areas since 2009. We know that buying or selling your home can be one of the most exciting (and sometimes trying) times of your life. Because of this, we make a concerted effort to know and understand your wants and needs, which plays a crucial part in both your success, and ours.</p>
  <div class="brand back-brand"><span class="brand__mark"></span>Meridian</div>
  <div class="back-contact">
    <div class="agent">Dale Carver Realtor</div>
    <div class="reach">Get in touch with us</div>
    <div class="phone">482-630-9157</div>
    <div class="web">thriveatharborview.com</div>
  </div>

  <div class="indicia">PRSRT STD<br>ECRWSS<br>U.S. Postage<br><b>PAID</b><br>EDDM RETAIL</div>
  <div class="address">Local<br>Postal Customer</div>
</section>

</body>
</html>
```